Business card/ stationary design for a pressure washing company
Commercial and Residential
Business card/ stationary design for a pressure washing company - Cleaning
Creative Brief
Simple
Marcus Delgado
N/A
Brookrinse@mailbox-demo.com
www.brookrinse-demo.com
Open to the idea of single or double sided business cards
brookrinse brookrinse
I have gone through the submissions that I have received so far and indicated a couple from each designer that I like. If you could please take that and apply it into a full stationary demo as well as a vehicle magnet, I would love to see how the design ideas transfer into the various applications. Thanks, Marcus
Also, a vehicle magnet would be very useful. Thanks!

```html
<!DOCTYPE html>
<html lang="en">
<head>
<meta charset="utf-8">
<title>Brookrinse Business Cards</title>
<link rel="stylesheet" href="https://fonts.googleapis.com/css2?family=Montserrat:wght@400;600;800&display=swap">
<style>
  :root {
    --backdrop: #3a3a3c;
    --card: #ffffff;
    --brand-blue: #1c4fc4;
    --deep-blue: #1a237e;
    --light-blue: #2f6fe0;
    --text-dark: #2b2b2b;
    --text-light: #ffffff;
  }
  * { margin: 0; padding: 0; box-sizing: border-box; }
  html, body { width: 1200px; height: 670px; overflow: hidden; }
  body {
    background: var(--backdrop);
    font-family: "Montserrat", sans-serif;
    position: relative;
  }
  .card {
    position: absolute;
    background: var(--card);
    overflow: hidden;
  }
  .card-front { left: 108px; top: 48px; width: 444px; height: 264px; }
  .card-back { left: 456px; top: 264px; width: 648px; height: 324px; }

  .brand {
    position: absolute;
    display: flex;
    align-items: center;
    gap: 12px;
    color: var(--brand-blue);
    font-weight: 800;
    text-transform: uppercase;
    letter-spacing: 1px;
    white-space: nowrap;
  }
  .brand-dot {
    border-radius: 50%;
    background: var(--brand-blue);
    flex: none;
  }
  .card-front .brand { left: 78px; top: 108px; font-size: 38px; }
  .card-front .brand-dot { width: 34px; height: 34px; }
  .card-back .brand { left: 40px; top: 76px; font-size: 33px; }
  .card-back .brand-dot { width: 30px; height: 30px; }

  .back-wave { position: absolute; inset: 0; width: 100%; height: 100%; }

  .holder { position: absolute; left: 80px; top: 200px; }
  .holder-name {
    color: var(--brand-blue);
    font-size: 15px;
    font-weight: 600;
    letter-spacing: 1px;
    text-transform: uppercase;
    white-space: nowrap;
  }
  .holder-title { color: var(--text-dark); font-size: 11.5px; margin-top: 4px; }

  .contact {
    position: absolute;
    left: 446px;
    top: 60px;
    color: var(--text-light);
    font-size: 11px;
    line-height: 1.55;
    list-style: none;
    white-space: nowrap;
  }
  .contact li { display: flex; align-items: center; gap: 8px; }
  .contact .gap { margin-top: 8px; }
  .contact svg { width: 11px; height: 11px; fill: var(--text-light); flex: none; }
</style>
</head>
<body>
  <section class="card card-front">
    <div class="brand"><span class="brand-dot"></span>Brookrinse</div>
  </section>

  <section class="card card-back">
    <svg class="back-wave" viewBox="0 0 648 324" preserveAspectRatio="none" aria-hidden="true">
      <path d="M0 300 C190 300 300 265 345 190 C375 135 382 45 405 0 L648 0 L648 324 L0 324 Z" fill="var(--deep-blue)"/>
      <path d="M0 324 L0 314 C200 314 318 280 365 205 C395 150 402 60 428 14 L648 14 L648 324 Z" fill="var(--light-blue)"/>
    </svg>

    <div class="brand"><span class="brand-dot"></span>Brookrinse</div>

    <div class="holder">
      <p class="holder-name">Marcus Delgado</p>
      <p class="holder-title">Managing Director</p>
    </div>

    <ul class="contact">
      <li>2841 Maple Road</li>
      <li>Lakeside Park 14B</li>
      <li class="gap"><svg viewBox="0 0 24 24"><path d="M6.6 10.8a15 15 0 0 0 6.6 6.6l2.2-2.2a1 1 0 0 1 1-.25 11.4 11.4 0 0 0 3.6.6 1 1 0 0 1 1 1V20a1 1 0 0 1-1 1A17 17 0 0 1 3 4a1 1 0 0 1 1-1h3.5a1 1 0 0 1 1 1c0 1.25.2 2.45.6 3.6a1 1 0 0 1-.25 1z"/></svg>(555) 014-2290</li>
      <li><svg viewBox="0 0 24 24"><path d="M6.6 10.8a15 15 0 0 0 6.6 6.6l2.2-2.2a1 1 0 0 1 1-.25 11.4 11.4 0 0 0 3.6.6 1 1 0 0 1 1 1V20a1 1 0 0 1-1 1A17 17 0 0 1 3 4a1 1 0 0 1 1-1h3.5a1 1 0 0 1 1 1c0 1.25.2 2.45.6 3.6a1 1 0 0 1-.25 1z"/></svg>(555) 014-3381</li>
      <li><svg viewBox="0 0 24 24"><path d="M6.6 10.8a15 15 0 0 0 6.6 6.6l2.2-2.2a1 1 0 0 1 1-.25 11.4 11.4 0 0 0 3.6.6 1 1 0 0 1 1 1V20a1 1 0 0 1-1 1A17 17 0 0 1 3 4a1 1 0 0 1 1-1h3.5a1 1 0 0 1 1 1c0 1.25.2 2.45.6 3.6a1 1 0 0 1-.25 1z"/></svg>(555) 014-4472</li>
      <li class="gap">Brookrinse@mailbox-demo.com</li>
      <li>www.brookrinse-demo.com</li>
    </ul>
  </section>
</body>
</html>
```